A combined poster for Martial arts club and Dance club.

We need a poster that will be hung opp and used in street bucks for advertisement. We are two independent clubs ( a dance studio and a MA gym) but have chosen to cooperate and split costs for advertisement. We also see an effect with both arts on the same poster.

We have a attached a picture with both arts doing a pose from each other. This would be great to use.

Target Market(s)

All ages primarily young people

Industry/Entity Type

Martial Art

Colors

Designer to choose colors to be used in the design.

Requirements
Must have
• A professional look. Both logos and either one of the attached pictures.
• Fight styles: Check webpage: http://www.kestrelforge.no
• Dance Styles: http://tramvikdansehus4.com
• Contact information Address and phone
• Space for texts slogans.
Nice to have
• Photoshop the picture with different background or cut them out.

```html
<!DOCTYPE html>
<html lang="no">
<head>
<meta charset="utf-8">
<title>Kestrel Forge &amp; Tramvik Dansehus 4</title>
<link rel="stylesheet" href="https://fonts.googleapis.com/css2?family=Oswald:wght@400;500;700&family=Roboto+Condensed:wght@400;700&display=swap">
<style>
  :root {
    --ink: #0b0c0e;
    --night: #16181c;
    --steel: #2a2d33;
    --red: #c8102e;
    --red-deep: #7d0a1c;
    --blue: #1f7fd0;
    --blue-deep: #0c3f73;
    --white: #ffffff;
    --mist: #c9cdd3;
  }
  * { margin: 0; padding: 0; box-sizing: border-box; }
  html, body { width: 849px; height: 1200px; overflow: hidden; background: var(--ink); }
  .poster {
    position: relative; width: 849px; height: 1200px; overflow: hidden;
    background: var(--ink); color: var(--white);
    font-family: "Oswald", sans-serif;
  }
  .hero-bg {
    position: absolute; left: 0; top: 0; width: 849px; height: 800px;
    background: linear-gradient(180deg, #3b3e45 0%, #2a2d33 55%, #17191d 100%);
  }
  .hero-photo {
    position: absolute; left: 150px; top: 40px; width: 520px; height: 730px;
    border-radius: 46% 46% 12% 12% / 30% 30% 8% 8%;
    background:
      radial-gradient(ellipse 110px 130px at 300px 260px, #b89a86 0%, rgba(184,154,134,0) 100%),
      radial-gradient(ellipse 200px 240px at 220px 430px, #e6e7ea 0%, rgba(230,231,234,0) 100%),
      radial-gradient(ellipse 160px 220px at 380px 560px, #6c7a92 0%, rgba(108,122,146,0) 100%),
      linear-gradient(180deg, #6e6f74 0%, #54575e 60%, #2e3036 100%);
  }
  .inset-photo { position: absolute; border: 3px solid #e9eaec; }
  .inset-left {
    left: 20px; top: 620px; width: 190px; height: 120px;
    background: linear-gradient(135deg, #4a5a78, #2a3448 70%, #8d95a3);
  }
  .inset-right {
    left: 650px; top: 400px; width: 170px; height: 190px;
    background: linear-gradient(160deg, #a08a6e, #5b4a3e 60%, #2d3340);
  }
  .bands { position: absolute; left: 0; top: 0; }
  .style-list {
    position: absolute; font-family: "Roboto Condensed", sans-serif; font-weight: 700;
    text-transform: uppercase; line-height: 1.25; font-size: 18px; letter-spacing: .3px;
    white-space: nowrap; text-shadow: 0 1px 3px rgba(0,0,0,.6);
  }
  .band-title {
    position: absolute; font-weight: 700; text-transform: uppercase;
    font-size: 50px; letter-spacing: 1px; white-space: nowrap; line-height: 1;
  }
  .dance-title { left: 548px; top: 38px; transform: rotate(22deg); transform-origin: left top; }
  .dance-list { left: 560px; top: 150px; transform: rotate(22deg); transform-origin: left top; }
  .fight-title { left: 22px; top: 372px; transform: rotate(-24deg); transform-origin: left top; }
  .fight-list {
    left: 330px; top: 60px; text-align: right;
    transform: translateX(-100%) rotate(-24deg); transform-origin: right top;
  }
  .footer {
    position: absolute; left: 0; top: 800px; width: 849px; height: 400px;
    background: linear-gradient(180deg, var(--night), var(--ink));
  }
  .divider { position: absolute; left: 424px; top: 50px; width: 1px; height: 260px; background: var(--steel); }
  .club { position: absolute; top: 60px; width: 424px; text-align: center; }
  .club-left { left: 0; }
  .club-right { left: 425px; }
  .club-name {
    display: inline-flex; align-items: center; gap: 12px;
    font-size: 32px; font-weight: 500; text-transform: uppercase; letter-spacing: 1.5px;
    color: var(--white); height: 110px;
  }
  .club-dot { width: 22px; height: 22px; border-radius: 50%; background: var(--blue); }
  .club-right .club-dot { background: var(--red); border-radius: 0; }
  .club-info {
    margin-top: 26px; font-family: "Roboto Condensed", sans-serif; font-size: 17px;
    line-height: 1.45; color: var(--mist); text-transform: uppercase;
  }
  .club-info .mail { font-size: 16px; }
  .phone {
    position: absolute; top: 352px; width: 424px; text-align: center;
    font-family: "Roboto Condensed", sans-serif; font-weight: 700; font-size: 22px;
  }
  .phone-left { left: 0; }
  .phone-right { left: 425px; }
</style>
</head>
<body>
<main class="poster">
  <div class="hero-bg"></div>
  <div class="hero-photo" role="img" aria-label="Martial artist in a white gi and dancer in a sparkling dress posing together"></div>
  <div class="inset-photo inset-left" role="img" aria-label="Group photo of martial arts students"></div>
  <div class="inset-photo inset-right" role="img" aria-label="Dancers performing on stage"></div>

  <svg class="bands" width="849" height="800" viewBox="0 0 849 800" aria-hidden="true">
    <polygon points="380,0 849,0 849,330" fill="var(--red-deep)"/>
    <polygon points="460,0 849,0 849,250" fill="var(--red)"/>
    <polygon points="0,300 600,110 0,500" fill="var(--blue-deep)"/>
    <polygon points="0,350 600,125 600,145 0,450" fill="var(--blue)"/>
    <path d="M0,770 Q420,690 849,600" fill="none" stroke="var(--red)" stroke-width="10"/>
    <path d="M0,790 Q430,720 849,640" fill="none" stroke="var(--blue)" stroke-width="8"/>
  </svg>

  <div class="band-title dance-title">Dance Styles</div>
  <div class="style-list dance-list">
    Jazz / Freestyle / Disco<br>
    Cheerleading / Basstrening<br>
    Barn/ungdom spesielle<br>
    Breakdance<br>
    Akrobatikk/Turn<br>
    Barnedans / Slowdance
  </div>

  <div class="band-title fight-title">Fight Styles</div>
  <div class="style-list fight-list">
    Brasiliansk jiu jitsu<br>
    Thaiboksing<br>
    Mixed martial arts<br>
    Submission wrestling<br>
    Kyokushin karate<br>
    Barn og ungdom
  </div>

  <footer class="footer">
    <section class="club club-left">
      <div class="club-name"><span class="club-dot"></span>Kestrel Forge</div>
      <div class="club-info">
        Brattlivegen 22<br>
        2015 Skjetten – 3 etg.<br>
        Mandag – Fredag: 17:00 – 20:30<br>
        Lørdag – Søndag: 12:00 – 14:00
      </div>
    </section>
    <div class="divider"></div>
    <section class="club club-right">
      <div class="club-name"><span class="club-dot"></span>Tramvik Dansehus 4</div>
      <div class="club-info">
        Brattlivegen 22,<br>
        2015 Skjetten<br><br>
        <span class="mail">post@tramvikdansehus4.com</span>
      </div>
    </section>
    <div class="phone phone-left">(+47) 900 11 234 / (+47) 900 55 678</div>
    <div class="phone phone-right">(+47) 60 00 12 34</div>
  </footer>
</main>
</body>
</html>
```